브랜드 소개
다온먹거리나눔진흥원는 『농수산식품산업 진흥을 통해 국민의 안정적인 먹거리 확보와 삶의질 향상에 기여』를 목표로 설립되어 유통개선·수급안정·수출진흥·식품산업육성 등의 사업을 수행하고 있습니다. 홈페이지는 공사 홍보 및 각종 공고 안내, 공사의 다양한 지원사업에 대한 창구 역할을 하고 있습니다. 다온먹거리나눔진흥원의 타겟은 농어업인과 소비자입니다.

```html
<!DOCTYPE html>
<html lang="ko">
<head>
<meta charset="utf-8">
<title>다온먹거리나눔진흥원 홈페이지</title>
<link href="https://fonts.googleapis.com/css2?family=Noto+Sans+KR:wght@400;500;700;900&display=swap" rel="stylesheet">
<style>
:root{
  --brand:#2f7d3a;
  --ink:#333333;
  --muted:#888888;
  --line:#e3e3e3;
  --blue:#4a9fc8;
  --green:#6aa84f;
  --red:#e2614a;
  --yellow:#e8b53a;
  --footer:#8c8c8c;
  --footer-dark:#6f6f6f;
  --page:#ffffff;
  --hero-a:#f2efe9;
}
*{box-sizing:border-box;margin:0;padding:0}
html,body{width:1200px;height:1200px;overflow:hidden;background:var(--page);font-family:"Noto Sans KR",sans-serif;color:var(--ink)}
.site{position:relative;width:1200px;height:1200px}
.util{height:32px;display:flex;justify-content:flex-end;align-items:center;gap:18px;padding:0 60px;font-size:12px;color:var(--muted);border-bottom:1px solid var(--line)}
.header{height:88px;display:flex;align-items:center;justify-content:space-between;padding:0 60px;border-bottom:1px solid var(--line)}
.logo{font-size:20px;font-weight:700;color:var(--brand);white-space:nowrap}
.gnb{display:flex;gap:44px;font-size:16px;font-weight:500}
.hero{position:relative;height:470px;background:var(--hero-a)}
.hero-photo-left{position:absolute;left:0;top:0;width:300px;height:100%;background:linear-gradient(160deg,#7d8790,#a4b09a 60%,#d9d6cd)}
.hero-photo-right{position:absolute;right:0;top:0;width:280px;height:100%;background:linear-gradient(200deg,#e0a23a,#7c9a4c 45%,#e8e4dc)}
.hero-copy{position:absolute;left:0;right:0;top:70px;text-align:center}
.hero-copy h1{font-size:40px;font-weight:900;line-height:1.35;color:#3a3a3a}
.hero-copy h1 em{font-style:normal;color:var(--red)}
.hero-copy p{margin-top:18px;font-size:14px;line-height:1.7;color:#666}
.quick{position:absolute;left:210px;top:520px;display:flex}
.card{width:190px;height:190px;padding:22px 20px;color:#fff;display:flex;flex-direction:column;justify-content:space-between}
.card h2{font-size:19px;font-weight:700;line-height:1.35}
.card .btn{align-self:flex-start;font-size:12px;background:rgba(255,255,255,.92);color:var(--ink);padding:4px 12px}
.card.blue{background:var(--blue)}.card.green{background:var(--green)}.card.red{background:var(--red)}.card.yellow{background:var(--yellow)}
.board{position:absolute;top:740px;left:60px;right:60px;display:flex;gap:40px}
.col{width:230px}
.col h3{font-size:16px;font-weight:700;padding-bottom:10px;border-bottom:2px solid var(--ink);margin-bottom:12px}
.col li{list-style:none;font-size:13px;color:#555;line-height:2.1;display:flex;justify-content:space-between}
.col li span{color:var(--muted)}
.services{display:flex;gap:40px;padding-top:20px}
.service{text-align:center;font-size:13px;color:#555}
.service svg{display:block;margin:0 auto 10px}
.social{display:flex;gap:8px;margin-top:40px}
.social i{width:22px;height:22px;border-radius:50%;display:block}
.footer{position:absolute;left:0;right:0;bottom:0;height:170px;background:var(--footer);color:#fff}
.footer-links{height:46px;background:var(--footer-dark);display:flex;align-items:center;gap:30px;padding:0 60px;font-size:13px}
.footer-body{display:flex;align-items:center;gap:40px;padding:30px 60px;font-size:13px;line-height:1.8}
.footer-logo{font-size:18px;font-weight:700;white-space:nowrap}
</style>
</head>
<body>
<div class="site">
  <div class="util"><span>로그인</span><span>회원가입</span><span>사이트맵</span><span>ENGLISH</span></div>
  <header class="header">
    <div class="logo">다온먹거리나눔진흥원</div>
    <nav class="gnb"><span>정보공개</span><span>고객참여</span><span>사업안내</span><span>경영공시</span><span>고객센터</span><span>공사소개</span></nav>
  </header>
  <section class="hero">
    <div class="hero-photo-left" role="img" aria-label="생선과 허브, 방울토마토가 놓인 식재료 사진"></div>
    <div class="hero-photo-right" role="img" aria-label="채소와 향신료, 잎채소가 놓인 식재료 사진"></div>
    <div class="hero-copy">
      <h1>대한민국 농수산 식품의<br><em>행복한 변화</em>가 시작됩니다!</h1>
      <p>다온먹거리나눔진흥원은 국민의 안정적인 먹거리 확보와 삶의 질 향상을 위해<br>농어업인과 소비자 모두가 행복한 내일을 만들어 갑니다.</p>
    </div>
  </section>
  <div class="quick">
    <div class="card blue"><h2>농수산식품<br>NEWS LETTER</h2><span class="btn">바로가기</span></div>
    <div class="card green"><h2>주요 농산물<br>유통가격 정보</h2><span class="btn">바로가기</span></div>
    <div class="card red"><h2>화훼 거래<br>시세 &amp; 가격표</h2><span class="btn">바로가기</span></div>
    <div class="card yellow"><h2>신규<br>채용 정보</h2><span class="btn">바로가기</span></div>
  </div>
  <section class="board">
    <div class="col"><h3>공지사항</h3><ul>
      <li>상반기 수출지원 사업 공고<span>04.12</span></li>
      <li>먹거리 나눔 캠페인 안내<span>04.08</span></li>
      <li>홈페이지 개편 안내<span>04.02</span></li>
      <li>유통정보 서비스 점검<span>03.28</span></li></ul></div>
    <div class="col"><h3>보도자료</h3><ul>
      <li>농식품 수출 실적 증가<span>04.11</span></li>
      <li>로컬푸드 직거래 확대<span>04.07</span></li>
      <li>수급안정 대책 발표<span>04.01</span></li>
      <li>식품산업 박람회 개최<span>03.25</span></li></ul></div>
    <div class="col"><h3>입찰정보</h3><ul>
      <li>비축물자 보관 용역<span>04.10</span></li>
      <li>물류센터 시설 보수<span>04.05</span></li>
      <li>홍보물 제작 입찰<span>03.30</span></li>
      <li>전산장비 유지 관리<span>03.22</span></li></ul></div>
    <div>
      <div class="services">
        <div class="service"><svg width="44" height="44" viewBox="0 0 44 44"><circle cx="22" cy="22" r="20" fill="none" stroke="#999" stroke-width="2"/><path d="M22 12v20M14 22h16" stroke="#999" stroke-width="2"/></svg>사이버 홍보관</div>
        <div class="service"><svg width="44" height="44" viewBox="0 0 44 44"><circle cx="22" cy="22" r="20" fill="none" stroke="#999" stroke-width="2"/><path d="M15 14c2 0 3 4 2 6l-1 1c1 3 3 5 6 6l1-1c2-1 6 0 6 2l-2 3c-8 0-14-6-14-14z" fill="#999"/></svg>고객센터</div>
      </div>
      <div class="social"><i style="background:#e2614a"></i><i style="background:#e8b53a"></i><i style="background:#6aa84f"></i><i style="background:#4a9fc8"></i><i style="background:#7a6ab0"></i></div>
    </div>
  </section>
  <footer class="footer">
    <div class="footer-links"><span>개인정보처리방침</span><span>이용약관</span><span>이메일무단수집거부</span><span>고객헌장</span><span>찾아오시는 길</span></div>
    <div class="footer-body">
      <div class="footer-logo">다온먹거리나눔진흥원</div>
      <div>대표전화 02-555-0148 · 다온시 나눔로 27<br>Copyright © 다온먹거리나눔진흥원. All rights reserved.</div>
    </div>
  </footer>
</div>
</body>
</html>
```